Luxury Lifestyle Website - Blog and Product Showcasing

I am looking to create a simple, yet elegant website where I can post blog posts and feature products and brand partnerships for my company, Velmora Haus. I want a very elegant but not overly complex site. I like the look and feel of Corinne Ashdale's site - I don't need for it to be that robust or sophisticated, but that is the aesthetic I am going for. I would like to include my primary logo at the top of the main page, and also incorporate my alternative logos throughout the site in strategic places.

Target Market(s)

Luxury Brands; 20s-60s year olds; women; high-end fashion and tastes

Industry/Entity Type

Luxury Lifestyle - Blogging - Product Showcasing

Coding

Coded - Design and coding required

Number of Pages Required

4 page

Font styles to use
Sans Serif
Script
Other font styles liked:
• Pinyon

Colors
00AB8E
00BBA5
67D7C9
C6EFE9
E9F9F6
59FF00
82FF00
B8FF75
E3FFCB
F4FFEA

Requirements
Must have
• Creative use of my various logos. PASTEL GREENS or a DEEP DARK GREEN. Nothing bright, very soft and elegant.
Nice to have
• Elegant script that is easy to read.
Should not have
• Bright colors or overly modern look or feel.

```html
<!DOCTYPE html>
<html lang="en">
<head>
<meta charset="utf-8">
<title>Velmora Haus — Luxury Lifestyle</title>
<link href="https://fonts.googleapis.com/css2?family=Arvo:wght@400;700&family=Pinyon+Script&family=Poppins:wght@300;400;500&display=swap" rel="stylesheet">
<style>
  :root{
    --ink:#1f3d36;
    --ink-soft:#3c5a52;
    --muted:#6d857e;
    --band:#1e463d;
    --band-deep:#173a32;
    --band-line:#c6efe9;
    --paper:#ffffff;
    --mint-50:#f4fbf9;
    --mint-100:#e9f9f6;
    --mint-200:#c6efe9;
    --mint-300:#67d7c9;
    --accent:#00ab8e;
    --slab:"Arvo", Georgia, serif;
    --sans:"Poppins", Arial, sans-serif;
    --script:"Pinyon Script", cursive;
  }
  *{margin:0;padding:0;box-sizing:border-box}
  html,body{width:1200px;height:4402px;overflow:hidden}
  body{position:relative;background:var(--paper);color:var(--ink);font-family:var(--sans)}
  .center-text{position:absolute;left:0;width:1200px;text-align:center}
  .photo{position:absolute}

  /* header */
  .site-header{position:absolute;top:0;left:0;width:1200px;height:70px}
  .menu-toggle{position:absolute;left:89px;top:26px;font-family:var(--slab);font-size:13px;color:var(--ink);display:flex;align-items:center;gap:6px}
  .brand{position:absolute;left:0;width:1200px;top:14px;text-align:center;font-family:var(--slab);font-size:28px;color:var(--ink)}
  .header-links{position:absolute;right:89px;top:26px;font-family:var(--slab);font-size:13px;display:flex;gap:22px;color:var(--ink)}

  /* hero */
  .hero{position:absolute;left:89px;top:77px;width:1022px;height:701px;
    background:linear-gradient(180deg,#dcd8d0 0%,#cfc8bd 45%,#8d7d6c 80%,#6f5f51 100%)}
  .hero-title{position:absolute;left:0;width:1022px;text-align:center;font-family:var(--slab);color:var(--band-deep)}
  .hero-eyebrow{top:112px;font-size:36px;letter-spacing:2px}
  .hero-main{top:148px;font-size:92px;font-weight:700;letter-spacing:3px;line-height:1.1}
  .hero-tag{top:238px;font-size:26px;letter-spacing:2px}
  .slider-dots{position:absolute;top:663px;left:395px;display:flex;gap:12px}
  .slider-dots span{height:2px;background:var(--mint-100);display:block}

  /* shared type */
  .eyebrow{font-family:var(--script);font-size:24px;line-height:26px;color:var(--accent)}
  .section-title{font-family:var(--slab);font-weight:700;font-size:34px;line-height:40px;color:var(--ink)}
  .section-sub{font-family:var(--slab);font-size:14px;color:var(--ink-soft)}
  .text-link{font-family:var(--slab);font-weight:700;font-size:13px;text-decoration:underline;color:inherit}

  /* intro cards */
  .topic-card{position:absolute;top:945px;width:264px;height:349px}
  .topic-card span{position:absolute;bottom:22px;left:0;width:100%;text-align:center;font-family:var(--slab);font-size:15px;color:#fff}

  /* about band */
  .about-band{position:absolute;left:0;top:1236px;width:1200px;height:606px;background:var(--band)}
  .monogram{position:absolute;left:190px;top:1450px;width:240px;text-align:center;font-family:var(--slab);font-size:40px;line-height:1.2;color:var(--mint-100)}
  .divider{position:absolute;left:467px;top:1362px;width:3px;height:369px;background:var(--band-line)}
  .about{position:absolute;left:528px;top:1410px;width:480px;color:#fff}
  .about .eyebrow{color:var(--mint-200);font-size:28px;line-height:30px}
  .about h2{font-family:var(--slab);font-weight:700;font-size:32px;margin:8px 0 14px}
  .about p{font-size:12.5px;line-height:20.5px;font-weight:300;color:var(--mint-100)}
  .about .text-link{display:inline-block;margin-top:12px;color:var(--mint-200)}

  /* lifestyle */
  .lifestyle{position:absolute;left:89px;top:1791px;width:1022px;height:511px;box-shadow:0 20px 50px rgba(30,70,61,.10)}
  .lifestyle-copy{position:absolute;left:0;top:0;width:511px;height:511px;background:var(--mint-100);text-align:center;padding:84px 56px 0}
  .lifestyle-copy .eyebrow{font-size:28px;line-height:30px}
  .lifestyle-copy h2{font-family:var(--slab);font-weight:700;font-size:34px;margin:0 0 12px;color:var(--ink)}
  .lifestyle-copy p{font-size:12.5px;line-height:20.5px;color:var(--muted);font-weight:300}
  .lifestyle-copy .catch{font-family:var(--slab);font-size:13px;color:var(--ink);margin-top:10px}
  .lifestyle-copy .text-link{display:inline-block;margin-top:16px;color:var(--ink)}

  /* shop */
  .shop-band{position:absolute;left:0;top:2740px;width:1200px;height:100px;background:var(--mint-100)}
  .product{position:absolute;top:2476px;width:248px;height:330px;background:#fff;box-shadow:0 10px 30px rgba(30,70,61,.08);text-align:center}
  .product .product-photo{position:absolute;left:44px;top:40px;width:160px;height:190px}
  .product h3{position:absolute;top:268px;width:100%;font-family:var(--slab);font-weight:400;font-size:13px;color:var(--ink-soft)}
  .product .price{position:absolute;top:288px;width:100%;font-family:var(--slab);font-weight:700;font-size:17px;color:var(--accent)}

  /* videos */
  .play{position:absolute;left:554px;top:3124px;width:92px;height:92px;border-radius:50%;background:rgba(233,249,246,.5)}
  .video-nav{position:absolute;top:3428px;font-family:var(--slab);font-weight:700;font-size:13px;color:var(--ink-soft)}

  /* spotlight */
  .spot{position:absolute;top:3618px;width:196px;height:197px}

  /* footer */
  .site-footer{position:absolute;left:0;top:3921px;width:1200px;height:481px;background:var(--band-deep);color:var(--mint-200)}
  .footer-brand{position:absolute;left:92px;top:152px;width:304px;text-align:center;font-family:var(--slab);font-size:34px;color:var(--mint-100)}
  .socials{position:absolute;left:140px;top:233px;display:flex;gap:12px}
  .socials span{width:42px;height:42px;border-radius:50%;border:2px solid rgba(198,239,233,.4);display:block}
  .foot-col{position:absolute;top:140px}
  .foot-col h4{font-family:var(--slab);font-weight:700;font-size:20px;color:#fff;margin-bottom:14px}
  .foot-col li{list-style:none;font-size:13.5px;line-height:30px;font-weight:300}
  .newsletter{position:absolute;left:895px;top:140px;width:213px}
  .newsletter h4{font-family:var(--slab);font-weight:700;font-size:18px;color:#fff;margin-bottom:14px}
  .newsletter .note{font-family:var(--slab);font-size:11px;margin-bottom:18px}
  .field{font-family:var(--slab);font-size:11px;border-bottom:1px solid rgba(198,239,233,.5);padding-bottom:6px;margin-bottom:16px}
  .newsletter .text-link{color:#fff;font-size:14px}
  .footer-rule{position:absolute;left:89px;top:430px;width:1022px;height:1px;background:rgba(198,239,233,.18)}
  .copyright{position:absolute;top:449px;left:0;width:1200px;text-align:center;font-size:11px;font-weight:500;color:#fff}
  .to-top{position:absolute;left:1130px;top:408px;width:44px;height:44px;border-radius:50%;background:var(--mint-100)}
</style>
</head>
<body>

<header class="site-header">
  <div class="menu-toggle">
    <svg width="14" height="10" viewBox="0 0 14 10"><path d="M0 1h14M0 5h10M0 9h14" stroke="#1f3d36" stroke-width="1.3"/></svg>
    Menu
  </div>
  <div class="brand">Velmora Haus</div>
  <nav class="header-links"><span>Search</span><span>Shop</span></nav>
</header>

<section class="hero" role="img" aria-label="Woman in a hat and red jacket relaxing on a deck chair by the river with a spritz on a small table">
  <div class="hero-title hero-eyebrow">VELMORA</div>
  <div class="hero-title hero-main">HAUS</div>
  <div class="hero-title hero-tag">LUXURY LIFESTYLE</div>
  <div class="slider-dots"><span style="width:48px"></span><span style="width:112px"></span><span style="width:52px"></span></div>
</section>

<div class="center-text eyebrow" style="top:827px">Introduction</div>
<h2 class="center-text section-title" style="top:855px">My Debut Book-Evergreen</h2>
<div class="center-text section-sub" style="top:901px">The wait is finally over...</div>

<div class="about-band"></div>
<div class="topic-card" style="left:185px;background:linear-gradient(180deg,#e7e4df,#b9a896 70%,#6b6560)" role="img" aria-label="Woman holding a beige jumper in front of a mirror"><span>In The Dressing Room</span></div>
<div class="topic-card" style="left:468px;background:linear-gradient(180deg,#f1f1f0,#d9d9d6 60%,#8a9080)" role="img" aria-label="White house entrance with hanging lamp and plants"><span>In The Home &amp; Gargen</span></div>
<div class="topic-card" style="left:750px;background:linear-gradient(180deg,#e4dccf,#c6a68a 60%,#9c846c)" role="img" aria-label="Woman in knitwear relaxing on a balcony hanging chair"><span>Lifestyle</span></div>

<div class="monogram">Velmora<br>Haus</div>
<div class="divider"></div>
<div class="about">
  <div class="eyebrow">About Us</div>
  <h2>Velmora Haus</h2>
  <p>It is a long established fact that a reader will be distracted by the readable content of a page when looking at its layout. The point of using Lorem Ipsum is that it has a more-or-less normal distribution of letters, as opposed to using 'Content here, content here', making it look like readable English. Many desktop publishing packages and web page editors now use Lorem Ipsum as their default model text, and a search for 'lorem ipsum' will uncover many web sites still</p>
  <a class="text-link">Read All</a>
</div>

<section class="lifestyle">
  <div class="lifestyle-copy">
    <div class="eyebrow">A Little Bit</div>
    <h2>Lifestyle</h2>
    <p>It is a long established fact that a reader will be distracted by the readable content of a page when looking at its layout. The point of using Lorem Ipsum is that it has a more-or-less normal distribution of letters, as opposed to using 'Content here, content here', making it look like readable English. Many desktop publishing packages and web page editors now use Lorem Ipsum as their default model text, and a search</p>
    <div class="catch">You can catch up on previous episodes below - enjoy!</div>
    <a class="text-link">View Lifestyle</a>
  </div>
  <div class="photo" style="left:511px;top:0;width:511px;height:511px;background:linear-gradient(180deg,#d6d2cc,#c4b4a2 55%,#9a8a7c)" role="img" aria-label="Two friends in hats laughing together at a riverside cafe terrace"></div>
</section>

<div class="shop-band"></div>

<div class="center-text eyebrow" style="top:2360px">Shop</div>
<h2 class="center-text section-title" style="top:2388px">My Shop</h2>
<div class="center-text section-sub" style="top:2434px">Things That Have Caught My Eye Recently...</div>

<div class="product" style="left:89px"><div class="product-photo" style="background:linear-gradient(180deg,#f3f3f3,#6b7790)" role="img" aria-label="Navy and white striped top"></div><h3>Product heading here</h3><div class="price">$25.00</div></div>
<div class="product" style="left:347px"><div class="product-photo" style="background:linear-gradient(180deg,#f6f1f2,#d9c0c6)" role="img" aria-label="White floral print midi dress"></div><h3>Product heading here</h3><div class="price">$25.00</div></div>
<div class="product" style="left:605px"><div class="product-photo" style="background:linear-gradient(180deg,#faf8f3,#e6e1d6)" role="img" aria-label="Cream tweed jacket and skirt set"></div><h3>Product heading here</h3><div class="price">$25.00</div></div>
<div class="product" style="left:863px"><div class="product-photo" style="background:linear-gradient(180deg,#e8d3a8,#1f1f1f)" role="img" aria-label="Beige and black slingback pumps"></div><h3>Product heading here</h3><div class="price">$25.00</div></div>

<div class="center-text eyebrow" style="top:2868px">Our Videos</div>
<h2 class="center-text section-title" style="top:2895px">Recent Videos</h2>

<div class="photo" style="left:0;top:2945px;width:258px;height:466px;background:linear-gradient(180deg,#d8d2ca,#8c6f5a 70%,#5d4a3c)" role="img" aria-label="Woman in a hat seated on a deck chair by the water"></div>
<div class="photo" style="left:268px;top:2945px;width:665px;height:466px;background:linear-gradient(180deg,#dcd6cc,#c5a88d 55%,#9d8a78)" role="img" aria-label="Woman in knitwear relaxing in a hanging chair on a balcony"></div>
<div class="play"><svg width="92" height="92" viewBox="0 0 92 92"><path d="M42 40 L52 46 L42 52 Z" fill="#1e463d"/></svg></div>
<div class="photo" style="left:943px;top:2945px;width:257px;height:466px;background:linear-gradient(180deg,#e3dbd0,#c88e64 60%,#9e7a62)" role="img" aria-label="Woman in a straw hat and rust dress sitting on a window seat"></div>

<div class="video-nav" style="left:89px">← Prev</div>
<div class="video-nav center-text" style="left:0">Keeping Secrets</div>
<div class="video-nav" style="left:1066px">Next →</div>

<div class="center-text eyebrow" style="top:3509px">In The Spotlight...</div>
<h2 class="center-text section-title" style="top:3536px">The Summer Tote Bag</h2>
<div class="center-text section-sub" style="top:3580px">If you're looking for an alternative to my Isabelle Varenne Tote...</div>

<div class="spot" style="left:89px;background:linear-gradient(180deg,#d9c9b6,#b49478)" role="img" aria-label="Woman in a straw hat and lace dress in a bright room"></div>
<div class="spot" style="left:296px;background:linear-gradient(180deg,#6e4a36,#b08a62)" role="img" aria-label="Woman in sunglasses and camel coat by a wooden door"></div>
<div class="spot" style="left:502px;background:linear-gradient(180deg,#d6d2cc,#f1eeea)" role="img" aria-label="Woman in a white suit on a city street"></div>
<div class="spot" style="left:709px;background:linear-gradient(180deg,#3a3836,#cfc8bf)" role="img" aria-label="Woman in white lounging on a sofa"></div>
<div class="spot" style="left:916px;background:linear-gradient(180deg,#5e5954,#e7e3dd)" role="img" aria-label="Woman in a white coat seated by a window"></div>

<a class="text-link center-text" style="top:3836px;color:var(--ink)">Read On</a>

<footer class="site-footer">
  <div class="footer-brand">Velmora Haus</div>
  <div class="socials" aria-label="Social links"><span></span><span></span><span></span><span></span></div>
  <div class="foot-col" style="left:485px">
    <h4>Quick links</h4>
    <ul><li>FAQ</li><li>Contact</li><li>Shop</li><li>Privacy Policy</li></ul>
  </div>
  <div class="foot-col" style="left:701px">
    <h4>Topics</h4>
    <ul><li>Dressing Room</li><li>Home &amp;</li><li>Garden</li><li>Lifestyle</li></ul>
  </div>
  <div class="newsletter">
    <h4>Velmora Haus</h4>
    <div class="note">Get Updates &amp; Exclusive News</div>
    <div class="field">First Name</div>
    <div class="field">Last Name</div>
    <a class="text-link">Subscribe</a>
  </div>
  <div class="footer-rule"></div>
  <div class="to-top"><svg width="44" height="44" viewBox="0 0 44 44"><path d="M22 28V16M17 21l5-5 5 5" fill="none" stroke="#1e463d" stroke-width="1.3"/></svg></div>
  <div class="copyright">© 2023 &nbsp;All Rights Reserved &nbsp;| &nbsp;Velmora Haus</div>
</footer>

</body>
</html>
```